Brochure Design Project

We are looking for a brochure to communicate the various different program we offer within the "Trailside & Habitat Studies" department
( www.fernpath.kx29.example.ca )
We have a large photo bank of students engaged in our programs and can willingly provide them if requested.

Target Market(s)

parents, students, academics, administrators

Industry/Entity Type

Bank

Requirements
Must have
• nature based theme. adventure and ecology.

```html
<!DOCTYPE html>
<html lang="en">
<head>
<meta charset="utf-8">
<title>Trailside &amp; Habitat Studies Brochure</title>
<link href="https://fonts.googleapis.com/css2?family=Tinos:ital,wght@0,400;0,700;1,700&family=Raleway:wght@200;300;400&family=Open+Sans:wght@700&display=swap" rel="stylesheet">
<style>
:root{
  --paper:#ffffff;
  --cream:#fcf8c6;
  --slate:#557782;
  --ink:#111111;
  --berry:#5b0a3d;
  --rust:#8d1c1c;
  --teal:#1f6f8c;
  --maroon:#7a1414;
  --sky:#3fc4e8;
  --ash:#8c8c8c;
  --night:#0b0b0b;
}
*{margin:0;padding:0;box-sizing:border-box}
html,body{width:1200px;height:1014px;overflow:hidden;background:var(--paper)}
.brochure{position:relative;width:1200px;height:1014px;font-family:"Tinos",serif;color:var(--ink)}

/* left panel */
.tips-frame{position:absolute;left:66px;top:22px;width:470px;height:507px;background:var(--slate);border-radius:0 0 10px 0}
.tips-title{position:absolute;left:74px;top:30px;width:40px;height:340px;display:flex;align-items:center;justify-content:center}
.tips-title span{transform:rotate(-90deg);white-space:nowrap;font-family:"Raleway",sans-serif;font-weight:300;font-size:27px;color:#e0412f;letter-spacing:.5px}
.tips-box{position:absolute;left:113px;top:23px;width:418px;height:490px;background:var(--cream);border:1px solid #333;padding:12px 12px 0 10px;font-size:14.6px;line-height:16.6px;text-align:justify}
.dropcap{float:left;font-size:64px;line-height:50px;margin:2px 4px 0 0}
.tips-box p{margin:0}
.section-q{position:absolute;left:66px;top:540px;width:470px;text-align:center;font-family:"Raleway",sans-serif;font-weight:300;font-size:21px;line-height:25px;color:var(--rust)}
.research{position:absolute;left:69px;top:597px;width:460px;font-size:14.6px;line-height:16.6px}
.research p{margin-bottom:16.6px}
.research .justify{text-align:justify}
.research .cap{float:left;font-size:50px;line-height:40px;margin:1px 3px 0 0}
.research a{color:var(--rust);text-decoration:none}

/* right panel */
.masthead{position:absolute;left:664px;top:22px;width:464px;height:88px;background:#f4efd6;border:1px solid #aaa}
.masthead .mark{position:absolute;left:14px;top:14px;width:58px;height:58px;background:var(--maroon)}
.masthead .district{position:absolute;left:130px;top:16px;font-family:"Open Sans",sans-serif;font-size:16px;color:var(--teal)}
.masthead .dept{position:absolute;left:130px;top:38px;font-family:"Tinos",serif;font-weight:700;font-size:20px;color:var(--maroon)}
.masthead .contact{position:absolute;left:130px;top:63px;font-family:"Open Sans",sans-serif;font-size:13px;color:#fff;text-shadow:1px 1px 0 #666,-1px 0 0 #888}
.story{position:absolute;left:664px;top:112px;width:464px;height:762px;background:var(--night)}
.story-photo{position:absolute;left:0;top:0}
.tagline{position:absolute;right:20px;top:240px;text-align:right;font-family:"Raleway",sans-serif;font-weight:200;color:#ddd}
.tagline .small{font-size:20px}
.tagline .big{font-size:30px;line-height:32px;color:#fff}
.tagline .big em{font-style:normal;color:var(--sky)}
.rule{position:absolute;left:64px;right:20px;top:326px;height:1px;background:#666}
.story h1{position:absolute;left:10px;right:10px;top:344px;text-align:center;font-family:"Open Sans",sans-serif;font-size:24.5px;line-height:30px;color:var(--ash)}
.story .about{position:absolute;left:18px;right:16px;top:416px;color:#fff;font-size:14.6px;line-height:16.6px;text-align:justify}
.about .cap{float:left;font-size:50px;line-height:40px;margin:1px 3px 0 0}
.about p{margin-bottom:16.6px}
.about .byline{font-weight:700;font-style:italic}
.partners{position:absolute;left:600px;top:884px;width:600px;height:76px;background:var(--night);display:flex;justify-content:center;gap:18px;padding-top:8px;padding-left:14px}
.partners i{display:block;width:68px;height:64px;background:#fff}

/* footer */
.band{position:absolute;left:0;width:1200px;background:var(--berry)}
.band.top{top:962px;height:24px}
.band.base{top:1005px;height:9px}
.footer-line{position:absolute;top:987px;font-family:"Raleway",sans-serif;font-weight:300;font-size:14px;color:#6a4a60}
.footer-line.left{left:108px}
.footer-line.right{left:868px}
</style>
</head>
<body>
<div class="brochure">

  <div class="tips-frame"></div>
  <div class="tips-title"><span>Ways to Get Outside!</span></div>
  <div class="tips-box">
    <p><span class="dropcap">W</span>ith over 80% of Canadians living in urban areas, our feet are more familiar with concrete than they are with the forest floor. Canadians spend over 90% of their time indoors and on average, six or more hours a day in front of a screen. This disconnection from the natural world is called Nature Deficit Disorder and is correlated with the increased incidence of obesity, heart disease, asthma, depression, and stress.</p>
    <p>Fortunately, the anecdote to this modern-day ailment is just beyond our front doors. Take time every day to take your vitamin O(utside)! Here is how:</p>
    <p>• Explore the wild places in your neighborhood.</p>
    <p>• Rediscover and reclaim your childhood wild places with your children.</p>
    <p>• Commit to sitting still in nature daily for a minimum of 20 minutes, and then share this experience with others by telling them about your solo time.</p>
    <p>• Find a local group that engages its members in outdoor recreation; meet new friends to get outdoors with!</p>
    <p>• Discover the names and uses of local flora and fauna in your region by investing in a plant or animal guidebook. You’ll be guiding interpretive walks in no time!</p>
    <p>• Get dirty, play in the mud, and jump in puddles!</p>
    <p>• Use nature as inspiration to create art, or better yet make natural art installments outside – think Mira Thornfield!</p>
    <p>• Create a garden, and enjoy the plethora of fruits born of this labor.</p>
  </div>

  <h2 class="section-q">Why is it important to spend time outdoors?<br>Well, here is what the research says!</h2>
  <div class="research">
    <p class="justify"><span class="cap">R</span>egular contact with nature promotes healthier social behavior and lessens social dysfunction, helps alleviate stress, improves resilience, promotes optimal psychological functioning, improves recovery from physical trauma, and reduces mortality.</p>
    <p>A child’s time in nature provides the benefits of creating sacred places, development of self and greater independence.<br>Children with ADHD who regularly play in green settings have milder symptoms than children who play in built outdoor and indoor settings.</p>
    <p>School gardens positively impact children’s learning and behavior.<br>Pregnant women living in areas with more trees had better birth outcomes.</p>
    <p class="justify" style="margin:0">Outdoor experience for teens has self-reported life-changing results. Children’s emotional affinity towards nature is a strong predictor of their willingness to protect the environment.<br>All research summarized &amp; provided by the Open Meadow Research Circle<br><a href="#">http://www.openmeadow.example.org/</a></p>
  </div>

  <header class="masthead">
    <div class="mark"></div>
    <div class="district">Kestrel Valley Schools</div>
    <div class="dept">Trailside &amp; Habitat Studies</div>
    <div class="contact">www.fernpath.kx29.example.ca 604 555-0147</div>
  </header>

  <section class="story">
    <svg class="story-photo" width="464" height="320" viewBox="0 0 464 320" role="img" aria-label="Photo of students in a circle on a sunlit forest meadow">
      <defs>
        <radialGradient id="sunlit" cx="0.3" cy="0.1" r="1">
          <stop offset="0" stop-color="#fff3a8"/>
          <stop offset="0.3" stop-color="#e8a526"/>
          <stop offset="0.65" stop-color="#6a3a10"/>
          <stop offset="1" stop-color="#1a0f06"/>
        </radialGradient>
      </defs>
      <path d="M0 0H464V180C330 185 120 200 0 310Z" fill="url(#sunlit)"/>
    </svg>
    <div class="tagline">
      <div class="small">Dedicated to Providing</div>
      <div class="big">Educational <em>Opportunities</em></div>
    </div>
    <div class="rule"></div>
    <h1>Trailside &amp; Habitat Studies<br>Department (KX29)</h1>
    <div class="about">
      <p><span class="cap">T</span>he Trailside &amp; Habitat Studies Department is dedicated to providing students with educational opportunities that reinforce their connection to the natural world and foster sustainability. We focus on giving students the necessary skills to think critically about personal choices and the relationships between society, economy, culture and the environment. Through action leadership, skill development and inspired experience, our students are empowered to make positive change in their communities. We offer numerous programs and have highlighted a few in this document.</p>
      <p style="margin:0">"The Trailside &amp; Habitat Studies Programs in Kestrel Valley Schools help to fill a huge void in modern society: the void between what’s taught in the classroom and the day-to-day miracles happening outside. I can think of no better way to close this gap than to get kids into wild areas where Nature does the teaching, affecting students in ways that stick with them for the rest of their lives."<br><span class="byline">- Dorian Calloway, Explorer, Wildlife Biologist, Author</span></p>
    </div>
  </section>

  <div class="partners"><i></i><i></i><i></i></div>

  <div class="band top"></div>
  <div class="footer-line left">connection to the natural world</div>
  <div class="footer-line right">connection to the natural world</div>
  <div class="band base"></div>
</div>
</body>
</html>
```